New Business Card Design Project

possibly double-sided card, with one side in color. leaves, a tree branch, or a tree of life, like laurel, olive, pine ... or a seed that grows. visual discreet and stylized or naive. no photo. no human silhouette Modern Typo possibly rounded corners matte paper, no selective varnish, neither gold nor silver English brief Double sided business card, with eventually a single colored side. Leaves, a tree branch or a tree of life, laurel, olive tree, pine tree ... or a growing seed. The design has to be discreet and stylized or naive. No human silhouettes Modern made Possibly rounded corners Matte paper, no selective varnish, no gold, no silver
Updates

I really prefer toned or subtles tones, Bluish / greenwich gray, verdigris ... Elegant and discreet colors Write "HUMANISTIC HYPNOTHERAPY, SYMBOLIC THERAPY" on 2 lines and on One side only (not with the name and address) Not use pictogram (such , address...)

Contact Information for Business Card

Hypnothérapie humaniste
Thérapie symbolique

Mireille Fontanel
Hypnothérapeute
06 48 17 35 82
84 rue des Glycines, 33320 Eysines
therapie.fontanel@exemplemail.fr

Colors
33b8a4
3176b5

Requirements
Must have
• sober, elegant and refined card Sober design, elegant, plain
Nice to have
• desired colors: gray, blue-gis, greyish, khaki ... Desired colors: gray, blue-gray, grayish green, khaki, ...
Should not have
• gaudy colors, bright greens no bright gold neon colors

```html
<!DOCTYPE html>
<html lang="fr">
<head>
<meta charset="utf-8">
<title>Mireille Fontanel – Hypnothérapeute</title>
<link rel="stylesheet" href="https://fonts.googleapis.com/css2?family=Jost:wght@300;400;500;600&display=swap">
<style>
  :root {
    --card-grey: #b3b3b2;
    --olive: #6c7045;
    --verdigris: #33b8a4;
    --blue: #3a7bc4;
  }
  html, body {
    margin: 0;
    padding: 0;
    width: 1200px;
    height: 686px;
    overflow: hidden;
    background: var(--card-grey);
  }
  .card {
    position: relative;
    width: 1200px;
    height: 686px;
    background: radial-gradient(ellipse at 60% 40%, #b9b9b8 0%, var(--card-grey) 70%);
    font-family: "Jost", sans-serif;
    overflow: hidden;
  }
  .tree-art {
    position: absolute;
    left: -40px;
    top: 28px;
    width: 325px;
    height: 450px;
    border-radius: 0 50% 45% 0 / 0 45% 55% 0;
    background: radial-gradient(ellipse at 35% 45%, #3fbfa6 0%, var(--verdigris) 55%, #5a9a7a 85%, rgba(108,112,69,0.6) 100%);
  }
  .specialties {
    position: absolute;
    right: 50px;
    top: 92px;
    margin: 0;
    text-align: right;
    color: var(--olive);
    line-height: 1;
  }
  .specialties .primary {
    display: block;
    font-weight: 300;
    font-size: 50px;
    letter-spacing: 0.5px;
  }
  .specialties .secondary {
    display: block;
    margin-top: 10px;
    font-weight: 500;
    font-size: 50px;
    letter-spacing: 1.5px;
  }
  .identity {
    position: absolute;
    right: 50px;
    top: 305px;
    text-align: right;
    color: var(--blue);
  }
  .identity .name {
    margin: 0;
    font-weight: 600;
    font-size: 26px;
  }
  .identity .role {
    margin: 18px 0 0;
    font-weight: 400;
    font-size: 25px;
  }
  .contact {
    position: absolute;
    right: 50px;
    top: 452px;
    color: var(--blue);
    font-size: 23px;
    font-weight: 400;
    font-style: normal;
    line-height: 1;
  }
  .contact .phone,
  .contact .email {
    display: block;
    text-align: right;
  }
  .contact .phone { margin-right: 7px; }
  .contact .email { margin-top: 24px; }
  .contact .address {
    display: block;
    margin-top: 24px;
    text-align: left;
    line-height: 28px;
  }
</style>
</head>
<body>
  <main class="card">
    <div class="tree-art" role="img" aria-label="Stylised tree branch with verdigris leaves on an olive trunk"></div>

    <h1 class="specialties">
      <span class="primary">HYPNOTHERAPIE HUMANISTE</span>
      <span class="secondary">THERAPIE SYMBOLIQUE</span>
    </h1>

    <div class="identity">
      <p class="name">Mireille Fontanel</p>
      <p class="role">Hypnothérapeute</p>
    </div>

    <address class="contact">
      <span class="phone">06 48 17 35 82</span>
      <span class="email">therapie.fontanel@exemplemail.fr</span>
      <span class="address">84 rue des Glycines,<br>33320 Eysines</span>
    </address>
  </main>
</body>
</html>
```